Calvanta Group Real Estate Company business cards

New business card design, we are generally happy with the basic layout of the existing front of business card, (feel free to change) but require a head shot photo on the back side.

http://www.calvanta.com.au/

Attached logos, and existing business card

------------------------------

Target Market(s)

Real estate

Industry/Entity Type

Real Estate

Contact Information for Business Card

Standard size double sided

Font styles to use
Other font styles liked:
• Futura

Requirements
Must have
• Photo head shot on the back side
Nice to have
• yes
Should not have
• No

```html
<!DOCTYPE html>
<html lang="en">
<head>
<meta charset="utf-8">
<title>Calvanta Group – Business Cards</title>
<link rel="stylesheet" href="https://fonts.googleapis.com/css2?family=Jost:wght@400;500&family=Open+Sans:wght@400;600;700&display=swap">
<style>
  :root {
    --stage: #e9e9ec;
    --brand-purple: #2f2263;
    --brand-purple-deep: #281c57;
    --brand-purple-soft: #35286b;
    --ink: #1d1d2b;
    --paper: #ffffff;
    --muted: #8a8a94;
    --photo-top: #c9c9cf;
    --photo-bottom: #2c3348;
  }
  * { box-sizing: border-box; margin: 0; padding: 0; }
  html, body { width: 1200px; height: 864px; overflow: hidden; }
  body {
    background: var(--stage);
    font-family: "Open Sans", Arial, sans-serif;
    position: relative;
  }
  .card {
    position: absolute;
    left: 310px;
    width: 580px;
    height: 355px;
    overflow: hidden;
    box-shadow: 0 4px 14px rgba(0,0,0,.18);
  }

  /* Photo side */
  .card--photo { top: 57px; background: var(--brand-purple); }
  .card__bands { position: absolute; inset: 0; }
  .headshot {
    position: absolute;
    left: 92px; top: 40px;
    width: 176px; height: 186px;
    border-radius: 50%;
    background: linear-gradient(180deg, var(--photo-top) 0%, #e6e6ea 45%, var(--photo-bottom) 100%);
    border: 3px solid var(--paper);
  }
  .photo-brand {
    position: absolute;
    left: 300px; top: 122px;
    width: 250px;
    text-align: center;
    color: var(--paper);
  }
  .photo-brand__name {
    font-family: "Jost", "Futura", sans-serif;
    font-weight: 400;
    font-size: 46px;
    line-height: 1;
    letter-spacing: 0.5px;
  }
  .photo-brand__tagline {
    margin-top: 22px;
    font-size: 13px;
    letter-spacing: 0.2px;
  }
  .photo-brand__services {
    margin-top: 18px;
    font-size: 15px;
    font-weight: 700;
    word-spacing: 3px;
  }

  /* Contact side */
  .card--contact { top: 452px; background: var(--paper); }
  .contact-brand {
    position: absolute;
    top: 48px; left: 0; right: 0;
    text-align: center;
    font-family: "Jost", "Futura", sans-serif;
    font-weight: 400;
    font-size: 70px;
    line-height: 1;
    color: var(--brand-purple);
  }
  .contact-list {
    position: absolute;
    right: 295px; top: 205px;
    list-style: none;
    text-align: right;
    font-size: 14px;
    color: var(--ink);
  }
  .contact-list li {
    display: flex;
    align-items: center;
    justify-content: flex-end;
    gap: 10px;
    height: 22px;
  }
  .contact-list svg { width: 12px; height: 12px; fill: var(--brand-purple); flex: none; }
  .person {
    position: absolute;
    left: 312px; top: 222px;
    color: var(--brand-purple);
  }
  .person__name { font-size: 20px; font-weight: 700; line-height: 1.1; }
  .person__role { font-size: 14px; color: var(--ink); }
  .company { margin-top: 18px; }
  .company__name { font-size: 16px; font-weight: 700; }
  .company__abn { font-size: 15px; color: var(--ink); }
  .company__abn b { color: var(--brand-purple); font-weight: 700; }
</style>
</head>
<body>

<section class="card card--photo" aria-label="Business card, photo side">
  <svg class="card__bands" viewBox="0 0 580 355" preserveAspectRatio="none" aria-hidden="true">
    <polygon points="60,0 210,0 120,355 0,355 0,250" fill="var(--brand-purple-soft)" opacity=".55"/>
    <polygon points="330,0 420,0 520,90 520,355 470,355 470,120" fill="var(--brand-purple-deep)" opacity=".7"/>
    <polygon points="420,0 580,0 580,200" fill="var(--brand-purple-soft)" opacity=".5"/>
  </svg>
  <div class="headshot" role="img" aria-label="Head shot of the director in a suit and tie"></div>
  <div class="photo-brand">
    <div class="photo-brand__name">calvanta group</div>
    <p class="photo-brand__tagline">let us show you property</p>
    <p class="photo-brand__services">Buy / Sell / Rent</p>
  </div>
</section>

<section class="card card--contact" aria-label="Business card, contact side">
  <div class="contact-brand">calvanta</div>
  <ul class="contact-list">
    <li>0412 586 304
      <svg viewBox="0 0 24 24" aria-hidden="true"><path d="M6.6 10.8a15.1 15.1 0 0 0 6.6 6.6l2.2-2.2a1 1 0 0 1 1-.25 11.4 11.4 0 0 0 3.6.57 1 1 0 0 1 1 1V20a1 1 0 0 1-1 1A17 17 0 0 1 3 4a1 1 0 0 1 1-1h3.5a1 1 0 0 1 1 1c0 1.25.2 2.45.57 3.57a1 1 0 0 1-.25 1z"/></svg>
    </li>
    <li>daniel.tran@calvanta.com.au
      <svg viewBox="0 0 24 24" aria-hidden="true"><path d="M2 5h20v14H2z M4 7v.4l8 5 8-5V7z" fill-rule="evenodd"/></svg>
    </li>
    <li>www.calvanta.com.au
      <svg viewBox="0 0 24 24" aria-hidden="true"><circle cx="12" cy="12" r="10"/></svg>
    </li>
  </ul>
  <div class="person">
    <p class="person__name">Daniel Tran</p>
    <p class="person__role">Director</p>
    <div class="company">
      <p class="company__name">Calvanta Group</p>
      <p class="company__abn"><b>ABN:</b> 51 824 763 190</p>
    </div>
  </div>
</section>

</body>
</html>
```